Store Promo Card (already have logo!)

I need a card design (single side) for my online women’s gift shop containing a promotional code to be placed in bags for attendees at an event. I’m flexible on both shape and sizing, but perhaps a 4x6 card.
—It should contain my attached logo, my website (www.corvidtpq.com), and my Instagram handle (@corvidtpq) and promotion language such as “15% off your purchase with code: MIRVOL”.
—I think I would like my logo to be large.
—It should be clean, simple and modern in design and should use the colors from my logo.
—I would like about 3-5 product pictures depending on design.
Target Market(s)
Women ages 30 to 60
Industry/Entity Type
Retail Upscale Gift
Look and feel

```html
<!DOCTYPE html>
<html lang="en">
<head>
<meta charset="UTF-8">
<title>Corvid TPQ Promo Card</title>
<link rel="stylesheet" href="https://fonts.googleapis.com/css2?family=Archivo+Black&family=Federo&family=Fira+Sans:wght@500;700&display=swap">
<style>
  :root {
    --blush: #f2d1da;
    --slate: #4d5e5e;
    --gold-dark: #c9790f;
    --gold-mid: #e2a72e;
    --gold-light: #fbee86;
    --flame-deep: #e8761a;
    --flame-bright: #fbd43a;
    --ink: #111111;
    --white: #ffffff;
  }
  * { margin: 0; padding: 0; box-sizing: border-box; }
  html, body { width: 800px; height: 1200px; overflow: hidden; background: var(--blush); }
  .card {
    position: relative;
    width: 800px;
    height: 1200px;
    background: var(--blush);
    overflow: hidden;
  }
  .brand-name {
    position: absolute;
    top: 70px;
    left: 0;
    width: 800px;
    text-align: center;
    font-family: "Archivo Black", sans-serif;
    font-weight: 400;
    color: var(--slate);
    line-height: 1;
  }
  .brand-name .brand-main { display: block; font-size: 104px; letter-spacing: 4px; }
  .brand-name .brand-sub { display: block; font-size: 30px; letter-spacing: 8px; margin-top: 26px; }

  .ribbon {
    position: absolute;
    left: 0;
    width: 800px;
    height: 31px;
    background: linear-gradient(90deg, var(--gold-dark) 0%, var(--gold-light) 18%, var(--gold-dark) 38%, var(--gold-mid) 62%, var(--gold-light) 86%, var(--gold-dark) 100%);
  }
  .ribbon-top { top: 341px; }
  .ribbon-bottom { top: 870px; }

  .offer-panel {
    position: absolute;
    top: 371px;
    left: 0;
    width: 800px;
    height: 499px;
    background: var(--slate);
  }

  .bow {
    position: absolute;
    left: 270px;
    width: 253px;
    height: 162px;
    border-radius: 50% 50% 40% 40%;
    background: radial-gradient(ellipse at center, var(--gold-light) 0%, var(--gold-mid) 45%, var(--gold-dark) 100%);
  }
  .bow-top { top: 290px; }
  .bow-bottom { top: 790px; }

  .offer-line {
    position: absolute;
    top: 494px;
    left: 0;
    width: 800px;
    text-align: center;
    font-family: "Federo", sans-serif;
    font-size: 38px;
    color: var(--white);
    letter-spacing: 1px;
    white-space: nowrap;
  }

  .coupon {
    position: absolute;
    top: 597px;
    left: 179px;
    width: 440px;
    height: 163px;
  }
  .coupon svg { position: absolute; inset: 0; }
  .coupon-code {
    position: absolute;
    inset: 0;
    display: flex;
    align-items: center;
    justify-content: center;
    font-family: "Archivo Black", sans-serif;
    font-size: 76px;
    color: var(--ink);
    letter-spacing: 1px;
    text-shadow: 2px 4px 4px rgba(0,0,0,0.35);
  }

  .follow {
    position: absolute;
    top: 993px;
    left: 0;
    width: 800px;
    text-align: center;
    font-family: "Fira Sans", sans-serif;
    font-weight: 700;
    font-size: 27px;
    color: var(--ink);
  }
  .follow span { border-bottom: 2px solid var(--ink); padding-bottom: 1px; letter-spacing: 0.5px; }

  .contact {
    position: absolute;
    left: 0;
    width: 800px;
    display: flex;
    justify-content: center;
    align-items: center;
    gap: 12px;
    font-family: "Fira Sans", sans-serif;
    font-weight: 500;
    font-size: 27px;
    color: var(--ink);
  }
  .contact-web { top: 1053px; }
  .contact-social { top: 1113px; }
  .contact svg { flex: none; }
</style>
</head>
<body>
<main class="card">
  <h1 class="brand-name"><span class="brand-main">CORVID</span><span class="brand-sub">TPQ</span></h1>

  <div class="offer-panel"></div>
  <div class="ribbon ribbon-top"></div>
  <div class="ribbon ribbon-bottom"></div>

  <div class="bow bow-top" role="img" aria-label="Gold satin ribbon bow tied over the top band"></div>
  <div class="bow bow-bottom" role="img" aria-label="Gold satin ribbon bow tied over the bottom band"></div>

  <p class="offer-line">15% OFF YOUR PURCHASE WITH CODE</p>

  <div class="coupon">
    <svg width="440" height="163" viewBox="0 0 440 163" aria-hidden="true">
      <defs>
        <linearGradient id="ticket-fill" x1="0" y1="0" x2="1" y2="1">
          <stop offset="0" stop-color="var(--flame-deep)"/>
          <stop offset="0.3" stop-color="var(--flame-bright)"/>
          <stop offset="0.6" stop-color="#f29a25"/>
          <stop offset="1" stop-color="var(--flame-bright)"/>
        </linearGradient>
      </defs>
      <path d="M22 4 H418 A18 18 0 0 0 436 22 V141 A18 18 0 0 0 418 159 H22 A18 18 0 0 0 4 141 V22 A18 18 0 0 0 22 4 Z"
            fill="url(#ticket-fill)" stroke="var(--flame-deep)" stroke-width="3"/>
      <line x1="30" y1="12" x2="400" y2="12" stroke="#fff6c8" stroke-width="2" stroke-linecap="round" opacity="0.8"/>
    </svg>
    <div class="coupon-code">MIRVOL</div>
  </div>

  <p class="follow"><span>FOR MORE UPDATES FOLLOW US</span></p>

  <p class="contact contact-web">
    <svg width="27" height="27" viewBox="0 0 24 24" aria-hidden="true">
      <circle cx="12" cy="12" r="10" fill="none" stroke="var(--ink)" stroke-width="2.4"/>
      <ellipse cx="12" cy="12" rx="4.2" ry="10" fill="none" stroke="var(--ink)" stroke-width="2.2"/>
      <line x1="2" y1="12" x2="22" y2="12" stroke="var(--ink)" stroke-width="2.2"/>
      <line x1="4" y1="7" x2="20" y2="7" stroke="var(--ink)" stroke-width="2"/>
      <line x1="4" y1="17" x2="20" y2="17" stroke="var(--ink)" stroke-width="2"/>
    </svg>
    www.corvidtpq.com
  </p>

  <p class="contact contact-social">
    <svg width="24" height="24" viewBox="0 0 24 24" aria-hidden="true">
      <circle cx="12" cy="12" r="10" fill="none" stroke="var(--ink)" stroke-width="2.4"/>
    </svg>
    @corvidtpq
  </p>
</main>
</body>
</html>
```